Ledgerwise Reach - B2B Demand Generation Website Project

We need a fully functional website for www.ledgerwisereach.example. We are a B2B Demand Generation company, based in London, working with companies such as QRT, VKD, Norvex, Brindlow, Tarvo generating them sales leads for their sales teams. We run this through digital marketing newsletter promotions and have a network of websites. Content syndication, data, demand generation, online marketing. Our logo has just been redone (attached) and we have a holding page already which i would like to use the style / colours. Our logo is bright and vibrant but i dont want the site to be a rainbow. We are expensive, classy, professorial, B2B, intelligent.

Home
About Us
Our Services
Prospora & QA Technology
Intent Data
Testimonials
Contact Us
Updates

Target Market(s)

B2B Marketers (QRT, Velquarion, Tarvo, VKD, Opal Reach, Driftmoor, Harlow Quantis, Technology Companies, Data Companies, Marketing Teams, Tumbleden.

Industry/Entity Type

Marketing

Coding

Coded - Design and coding required

Number of Pages Required

5+ page

Font styles to use
Sans Serif

Requirements
Must have
• Home
About Us
Our Services
Prospora & QA Technology
Intent Data
Testimonials
Contact Us

Simple Pages.

Look classy, intelligent, data experts. I like the video homepages were the image moves at the top. Very soft animation.
Nice to have
• Websites i like:

https://www.vkd.example/
https://www.brevantor.example/
https://www.plumfieldsites.example.co.uk/

Ledgerwise Reach - The Demand Generation Company
Should not have
• Glimpsevault crap images

```html
<!DOCTYPE html>
<html lang="en">
<head>
<meta charset="utf-8">
<title>Ledgerwise Reach – Our Service</title>
<link href="https://fonts.googleapis.com/css2?family=Didact+Gothic&family=Questrial&display=swap" rel="stylesheet">
<style>
:root{
  --navy:#0b1f4a;
  --navy-deep:#06122e;
  --brand-blue:#1b4f91;
  --bright-blue:#1e8ff0;
  --link-blue:#1f5ea8;
  --red:#d3202a;
  --text:#3d3d3d;
  --grey-bg:#f6f6f7;
  --white:#ffffff;
}
*{margin:0;padding:0;box-sizing:border-box}
html,body{width:1200px;height:3192px;overflow:hidden;background:var(--white)}
body{position:relative;font-family:"Didact Gothic",sans-serif;color:var(--text)}

/* hero */
.hero{position:absolute;left:0;top:0;width:1200px;height:510px;
  background:radial-gradient(ellipse at 50% 40%,#1a3f85 0%,#0d2558 45%,var(--navy-deep) 100%);overflow:hidden}
.nav-band{position:absolute;left:380px;top:72px;width:820px;height:87px;
  background:linear-gradient(90deg,rgba(30,90,180,0.35),rgba(30,100,200,0.75));}
.brand{position:absolute;left:87px;top:60px;display:flex;align-items:center;gap:12px;color:var(--white)}
.brand-dot{width:40px;height:40px;border-radius:50%;border:2px solid var(--white)}
.brand-name{font-family:"Questrial",sans-serif;font-size:28px;line-height:1}
.brand-tag{position:absolute;left:139px;top:134px;font-size:9px;color:var(--white);font-family:"Questrial",sans-serif}
.social{position:absolute;display:flex;gap:11px}
.social span{width:15px;height:15px;border-radius:50%;background:var(--white)}
.contact-btn{position:absolute;left:968px;top:19px;width:142px;height:41px;border:1.5px solid var(--white);
  color:var(--white);font-size:15px;display:flex;align-items:center;justify-content:center;font-family:"Questrial",sans-serif}
.nav a{position:absolute;top:109px;color:var(--white);font-size:15px;text-decoration:none;font-family:"Questrial",sans-serif;letter-spacing:.2px}
.nav a.active{font-weight:bold;font-family:"Didact Gothic",sans-serif}
.nav a.active::after{content:"";position:absolute;left:0;right:0;top:24px;height:2px;background:var(--white)}
.hero-title{position:absolute;left:0;width:1200px;top:248px;text-align:center;color:var(--white);
  font-family:"Questrial",sans-serif;font-size:47px;font-weight:normal}
.hero-sub{position:absolute;left:270px;width:660px;top:314px;text-align:center;color:var(--white);
  font-size:22px;line-height:32px}
.hero-rule{position:absolute;left:540px;top:414px;width:113px;height:2px;background:var(--white)}
.torn{position:absolute;left:0}

/* sections */
.band-grey{position:absolute;left:0;top:1122px;width:1200px;height:893px;background:var(--grey-bg)}
.sec-title{position:absolute;font-family:"Questrial",sans-serif;font-size:37px;line-height:51px;color:var(--brand-blue);font-weight:normal}
.sec-body{position:absolute;font-size:15.5px;line-height:19px;letter-spacing:.3px;text-align:justify;color:var(--text)}
.sec-body p{margin-bottom:19px}
.sec-body.tight p{margin-bottom:0}
.sec-rule{position:absolute;width:143px;height:2px;background:linear-gradient(90deg,var(--brand-blue),var(--red))}
.visual{position:absolute;border-radius:50%}

/* footer */
.footer-brand{position:absolute;left:0;width:1200px;top:2712px;display:flex;justify-content:center;align-items:center;gap:12px}
.footer-brand .brand-dot{border-color:var(--red);width:44px;height:44px}
.footer-brand .brand-name{color:var(--red);font-size:32px}
.footer-tag{position:absolute;left:0;width:1200px;top:2790px;text-align:center;font-size:10px;color:var(--brand-blue)}
.fcol h4{position:absolute;font-size:17px;font-weight:bold;color:var(--brand-blue);font-family:"Didact Gothic",sans-serif}
.flink{position:absolute;font-size:16px;color:var(--link-blue)}
.fsocial span{background:var(--navy)}
.to-top{position:absolute;left:1029px;top:2988px;width:54px;height:54px;border-radius:50%;
  background:linear-gradient(135deg,var(--brand-blue),var(--red));display:flex;align-items:center;justify-content:center}
.bottom-bar{position:absolute;left:0;top:3118px;width:1200px;height:74px;
  background:linear-gradient(90deg,var(--brand-blue),#3b3a78 50%,#b0101c)}
.bottom-bar p{position:absolute;left:176px;top:32px;font-size:13px;color:var(--white)}
</style>
</head>
<body>

<header class="hero">
  <div class="nav-band"></div>

  <div class="brand"><span class="brand-dot"></span><span class="brand-name">Ledgerwise Reach</span></div>
  <div class="brand-tag">The Demand Generation Company</div>

  <div class="social" style="left:800px;top:31px"><span></span><span></span><span></span><span></span></div>
  <div class="contact-btn">CONTACT US</div>

  <nav class="nav">
    <a style="left:441px">HOME</a>
    <a style="left:532px">ABOUT</a>
    <a class="active" style="left:628px">SERVICES</a>
    <a style="left:744px">QA TECHNOLOGY</a>
    <a style="left:927px">INTEND DATA</a>
    <a style="left:1071px">NEWS</a>
  </nav>

  <h1 class="hero-title">Our Service</h1>
  <p class="hero-sub">multi-channel demand generation services to publishers and technology vendors through</p>
  <div class="hero-rule"></div>
</header>
<svg class="torn" style="top:482px" width="1200" height="34" viewBox="0 0 1200 34" aria-hidden="true">
  <path d="M0 14 L40 8 L80 16 L130 6 L180 14 L240 9 L300 17 L360 8 L420 15 L480 7 L540 16 L600 9 L660 15 L720 6 L780 14 L840 8 L900 17 L960 9 L1020 15 L1080 7 L1140 14 L1200 9 V34 H0 Z" fill="#ffffff"/>
</svg>

<section>
  <h2 class="sec-title" style="left:180px;top:585px">Marketing Qualified<br>Leads (MQL)</h2>
  <div class="sec-body" style="left:176px;top:722px;width:469px">
    <p>A Marketing Qualified Lead (MQL) is a prospect that has expressed an interest in what your brand has to offer. An MQL has taken the first steps to becoming a customer and is ready to receive additional contact from your company. From a very general perspective: Marketing Qualified Leads turn into Sales Qualified Leads (SQLs), which in turn can convert into customers once they have been through the buyer’s journey.</p>
    <p>It’s important for each potential customer to travel through all stages of the buying journey and the MQL is the first step in this process. This engagement warms them up to your brand, builds trust and puts them in the position to consider your solution as the right fit for their business.</p>
    <p>The MQL is the foundation of a B2B demand generation strategy and helps businesses identify those prospects who could be in the market for their solutions.</p>
  </div>
  <div class="sec-rule" style="left:176px;top:1089px"></div>
  <div class="visual" role="img" aria-label="Photo of a person using a smartphone with floating app icons, framed in a speech-bubble circle"
       style="left:732px;top:682px;width:322px;height:322px;background:radial-gradient(circle at 60% 45%,#d8c4b8,#9a8a84 60%,#6a6a78);border:4px solid var(--red);border-left-color:var(--brand-blue)"></div>
</section>

<div class="band-grey"></div>
<svg class="torn" style="top:1110px" width="1200" height="24" viewBox="0 0 1200 24" aria-hidden="true">
  <path d="M0 12 L60 6 L120 14 L190 5 L260 13 L330 7 L400 15 L470 6 L540 13 L610 7 L680 14 L750 5 L820 13 L890 6 L960 14 L1030 7 L1100 13 L1200 8 V24 H0 Z" fill="#f6f6f7"/>
</svg>
<section>
  <h2 class="sec-title" style="left:605px;top:1213px">Account Based<br>Marketing Leads (ABM)</h2>
  <div class="sec-body" style="left:601px;top:1350px;width:463px">
    <p>ABM is a strategy that directs marketing resources to engaging a specific set of target accounts.</p>
    <p>Instead of casting a wide net to engage any potential customers, marketers use ABM and work closely with sales to identify key prospects and then tailor customized programs and messages to the buying team within target accounts. This approach looks at prospects as Accounts rather than Individuals and takes the approach that in order to win business we must look at all stakeholders in the decision-making process.</p>
    <p>This strategy is particularly important in today’s world of work, as according to Corvanta, 73% of B2B buyers are now millennials and millennials actively seek consensus and collaboration. This has created a culture of “We” not “I” in the way technology purchasing decisions are made.</p>
    <p>Adopting an intelligent ABM strategy for demand generation can be a great way to target potential new customers. But it must be done right…</p>
    <p>The accounts you are looking to target must have intelligence behind them for the campaign to be considered a true ABM campaign. We can help with in this process of identifying accounts you should be targeting through our Intent partnerships and own first party data and speak to you about other strategies that have been successful in the past.</p>
  </div>
  <div class="sec-rule" style="left:602px;top:1925px"></div>
  <div class="visual" role="img" aria-label="Illustration of a hand pointing at a network of connected people icons inside a bright blue speech-bubble circle"
       style="left:207px;top:1313px;width:300px;height:300px;background:radial-gradient(circle at 45% 40%,#37c3ec,#1a9fd6 70%,#1488c4)"></div>
</section>
<svg class="torn" style="top:2003px" width="1200" height="24" viewBox="0 0 1200 24" aria-hidden="true">
  <path d="M0 12 L70 5 L140 13 L210 6 L280 14 L350 7 L420 13 L490 5 L560 14 L630 7 L700 13 L770 6 L840 14 L910 7 L980 13 L1050 5 L1120 14 L1200 8 V24 H0 Z" fill="#ffffff"/>
</svg>

<section>
  <h2 class="sec-title" style="left:174px;top:2086px">Sales Qualified Lead /<br>BANT</h2>
  <div class="sec-body tight" style="left:176px;top:2209px;width:463px">
    <p>An SQL lead or a BANT lead is a type of lead that expressed a specific interest in a product and service that you have to offer…</p>
    <p>The difference between marketing qualified leads (MQL) and sales qualified leads (SQL) is important to understanding your sales funnel, and perhaps most importantly, the potential bottlenecks within it.</p>
    <p>SQLs are prospects that have been vetted to determine if there’s an interest to connect them to the next stage in the buying cycle, sometimes called the Discovery or Demo stage.</p>
    <p>Commonly, BANT qualification methodology has been used by sales to define what constitutes a ‘quality’ lead. Budget, Authority, Need, and Timing are all criteria that need to be established but are they sufficient enough to enable your sales team to close a deal.</p>
    <p>We are able to offer BANT / SQL leads globally whether the target is IT, Hr, Marketing &amp; Sales. Finance or Business Decision Makers.</p>
  </div>
  <div class="sec-rule" style="left:176px;top:2602px"></div>
  <div class="visual" role="img" aria-label="Photo of a smiling professional beneath a network diagram of connected contact icons, framed in a speech-bubble circle"
       style="left:729px;top:2170px;width:322px;height:322px;background:radial-gradient(circle at 50% 45%,#e6eef6,#b9cde0 65%,#8ea6c2);border:4px solid var(--red);border-left-color:var(--brand-blue)"></div>
</section>

<footer>
  <div class="footer-brand"><span class="brand-dot"></span><span class="brand-name">Ledgerwise Reach</span></div>
  <div class="footer-tag">The Demand Generation Company</div>

  <div class="fcol">
    <h4 style="left:176px;top:2848px">Menu</h4>
    <a class="flink" style="left:176px;top:2889px">Home</a>
    <a class="flink" style="left:176px;top:2924px">QA Technology</a>
    <a class="flink" style="left:176px;top:2955px">About Us</a>
    <a class="flink" style="left:176px;top:2987px">Services</a>
    <a class="flink" style="left:176px;top:3019px">Intent Data</a>
    <a class="flink" style="left:176px;top:3050px">Latest News</a>

    <h4 style="left:394px;top:2848px">Useful Link</h4>
    <a class="flink" style="left:394px;top:2889px">Contact Us</a>
    <a class="flink" style="left:394px;top:2927px">Terms &amp; Condition</a>
    <a class="flink" style="left:394px;top:2961px">Privacy Policy</a>
    <a class="flink" style="left:394px;top:2993px">Copy Rights</a>

    <h4 style="left:610px;top:2848px">Contact</h4>
    <p class="flink" style="left:610px;top:2893px">Phone: +000 999 112</p>
    <p class="flink" style="left:610px;top:2941px">Email:lorem@info.example</p>
    <p class="flink" style="left:610px;top:2989px;line-height:23px">Address: lorem ipsum<br>content , address place.</p>

    <h4 style="left:866px;top:2848px">Follow Us</h4>
    <div class="social fsocial" style="left:866px;top:2893px"><span></span><span></span><span></span><span></span></div>
  </div>

  <div class="to-top" aria-label="Back to top">
    <svg width="26" height="16" viewBox="0 0 26 16" aria-hidden="true"><path d="M3 13 L13 4 L23 13" fill="none" stroke="#fff" stroke-width="4" stroke-linecap="round" stroke-linejoin="round"/></svg>
  </div>

  <div class="bottom-bar"><p>© 2020 Ledgerwise Reach. All rights reserved.</p></div>
</footer>

</body>
</html>
```